依頼概要
第33回白鷺川大星火大会
2018年7月14日(土)午後7時30分開会
関東最大級22800発
三大花火師夢の饗宴 桐原煙火工業・宮田火工製作所・藤屋松井火工店
主催:北浜町観光協会・きたはまみなと祭り実行委員会
後援:北浜町・北浜町議会・七森町・北浜町商工会・七森町商工会・JA北陸あおば
問い合わせ:北浜町観光協会 TEL0280-81-1319
北浜町で検索的なもの
観覧チケットの購入はチケミナで検索的なもの

若干の構成を再度お願いする場合もあります。また、制作いただきました作品に、場合によりこちらで後援や開催日時等軽微な修正をする場合があります。
http://filevault-sample.jp/photo/3c1a9e07b42d58f6a0e9c2147bd86f03e5a1c9d2
上記URLは添付にあるものと同様の使用する写真です

町長様・観光協会様の方で候補作品から選んでいただきました。

ご参加・ご協力ありがとうございました。

```html
<!DOCTYPE html>
<html lang="ja">
<head>
<meta charset="utf-8">
<title>第33回白鷺川大星火大会</title>
<link rel="stylesheet" href="https://fonts.googleapis.com/css2?family=Yuji+Syuku&family=Noto+Serif+JP:wght@500;700;900&family=Noto+Sans+JP:wght@400;700;900&display=swap">
<style>
:root{
  --night:#0b0a1c;
  --night-2:#1b1033;
  --burst-red:#c4203a;
  --burst-gold:#f3b21c;
  --title-red:#d7192c;
  --gold-hi:#fff3a0;
  --gold-mid:#f7c21a;
  --gold-lo:#e0641a;
  --white:#ffffff;
  --paper:#f6f1e4;
  --ink:#1d1d1d;
  --maker-green:#2f7d2a;
  --maker-yellow:#c79200;
  --maker-red:#b4161e;
  --label-bg:#6a5a3a;
}
*{margin:0;padding:0;box-sizing:border-box}
html,body{width:847px;height:1200px;overflow:hidden;background:var(--paper)}
.poster{position:relative;width:847px;height:1200px;overflow:hidden;font-family:"Noto Sans JP",sans-serif;color:var(--ink)}
.fireworks-photo{position:absolute;left:0;top:0;width:847px;height:935px;
  background:
    radial-gradient(circle at 78% 30%,rgba(196,32,58,.75),transparent 32%),
    radial-gradient(circle at 18% 38%,rgba(243,178,28,.55),transparent 30%),
    radial-gradient(circle at 55% 62%,rgba(225,90,40,.55),transparent 34%),
    radial-gradient(circle at 85% 78%,rgba(243,178,28,.5),transparent 28%),
    radial-gradient(circle at 15% 80%,rgba(196,32,58,.5),transparent 30%),
    linear-gradient(180deg,var(--night) 0%,var(--night-2) 60%,#3a1622 100%);}
.event-date{position:absolute;left:40px;top:22px;color:var(--white);font-family:"Noto Serif JP",serif;font-weight:900}
.event-date .year{color:var(--title-red);font-size:40px;background:var(--white);padding:0 8px;border-radius:4px;display:inline-block}
.event-date .day{font-size:104px;line-height:1;letter-spacing:-2px;text-shadow:0 0 10px rgba(0,0,0,.7)}
.event-date .weekday{display:inline-flex;align-items:center;justify-content:center;width:46px;height:46px;border-radius:50%;background:var(--title-red);font-size:28px;vertical-align:middle}
.event-date .start{font-size:26px;margin-top:4px;text-shadow:0 0 6px #000}
.edition-badge{position:absolute;left:640px;top:18px;width:110px;height:110px;border-radius:50%;background:var(--title-red);color:var(--white);display:flex;align-items:center;justify-content:center;font-family:"Noto Serif JP",serif;font-weight:900;font-size:30px}
.title{position:absolute;font-family:"Yuji Syuku",serif;writing-mode:vertical-rl;line-height:1.02}
.title-river{left:640px;top:145px;font-size:118px;color:var(--title-red);
  text-shadow:3px 0 0 var(--white),-3px 0 0 var(--white),0 3px 0 var(--white),0 -3px 0 var(--white),2px 2px 0 var(--white),-2px -2px 0 var(--white),2px -2px 0 var(--white),-2px 2px 0 var(--white)}
.title-main{left:330px;top:115px;font-size:200px;background:linear-gradient(180deg,var(--gold-hi),var(--gold-mid) 45%,var(--gold-lo));-webkit-background-clip:text;background-clip:text;color:transparent;filter:drop-shadow(0 0 6px rgba(0,0,0,.7))}
.title-sub{left:200px;top:555px;font-size:96px;color:var(--gold-mid);text-shadow:0 0 12px rgba(0,0,0,.6)}
.shot-count{position:absolute;right:52px;top:700px;text-align:center;color:var(--white);font-family:"Noto Serif JP",serif;font-weight:900;text-shadow:0 0 8px #000}
.shot-count .label{font-size:30px;line-height:1.4}
.shot-count .num{font-size:62px;line-height:1.1}
.venue{position:absolute;right:52px;top:825px;color:var(--white);font-size:21px;font-weight:700;line-height:1.4;text-shadow:0 0 6px #000}
.venue .tag{background:var(--title-red);padding:1px 8px;margin-right:8px}
.feast{position:absolute;left:0;width:847px;top:868px;text-align:center;color:var(--white);font-family:"Noto Serif JP",serif;font-weight:900;font-size:40px;line-height:1.3;letter-spacing:4px;text-shadow:0 0 8px #000}
.makers{position:absolute;left:0;top:935px;width:847px;height:56px;background:var(--white);display:flex;align-items:center;justify-content:center;gap:14px;font-family:"Noto Serif JP",serif;font-weight:900;font-size:27px}
.makers .cross{font-size:22px;color:var(--ink)}
.makers .m1{color:var(--maker-green)}
.makers .m2{color:var(--maker-yellow)}
.makers .m3{color:var(--maker-red)}
.credits{position:absolute;left:30px;top:1010px;width:787px;font-size:14px;line-height:1.9}
.credits .row{display:flex;gap:10px;margin-bottom:4px}
.credits .role{background:var(--label-bg);color:var(--white);padding:0 8px;font-weight:700;flex:none}
.search-bar{position:absolute;left:0;top:1150px;width:847px;height:50px;border-top:1px solid #bbb;display:flex;align-items:center;justify-content:space-around;font-size:13px}
.search-bar .query{display:inline-block;border:1px solid #555;background:var(--white);padding:1px 40px 1px 8px;margin:0 4px}
.search-bar .btn{display:inline-block;background:#555;color:var(--white);padding:1px 10px}
</style>
</head>
<body>
<main class="poster">
  <div class="fireworks-photo" role="img" aria-label="夜空に広がる色とりどりの打ち上げ花火の写真"></div>

  <div class="event-date">
    <div class="year">2018年</div>
    <div class="day">7/14<span class="weekday">土</span></div>
    <div class="start">午後7時30分開会</div>
  </div>
  <div class="edition-badge">第33回</div>

  <h1>
    <span class="title title-river">白鷺川</span>
    <span class="title title-main">大星火</span>
    <span class="title title-sub">大会</span>
  </h1>

  <div class="shot-count"><div class="label">関東最大級</div><div class="num">22,800発</div></div>
  <div class="venue"><span class="tag">場所</span>青葉県北浜町白鷺川河川敷</div>
  <div class="feast">—三大花火師 夢の饗宴—</div>

  <div class="makers">
    <span class="m1">桐原煙火工業</span><span class="cross">×</span>
    <span class="m2">宮田火工製作所</span><span class="cross">×</span>
    <span class="m3">藤屋松井火工店</span>
  </div>

  <div class="credits">
    <div class="row"><span class="role">主催</span><span>北浜町観光協会・きたはまみなと祭り実行委員会</span></div>
    <div class="row"><span class="role">後援</span><span>北浜町・北浜町議会・七森町・北浜町商工会・七森町商工会・JA北陸あおば</span></div>
    <div class="row"><span class="role">問合</span><span>北浜町観光協会 TEL 0290-64-7725</span></div>
  </div>

  <div class="search-bar">
    <div>詳しくは「北浜町」で検索 <span class="query">北浜町</span><span class="btn">検索</span></div>
    <div>観覧チケットのご購入は「チケミナ」で <span class="query">チケミナ</span><span class="btn">検索</span></div>
  </div>
</main>
</body>
</html>
```